QuartzNook Works, LLC Corporate Web Site

The goal of this web site is simple. To provide an information and corporate information site for people who click on company links from other web sites. Put simply, this web site is primarily a brochure web site for the parent business. It will contain information about the company and our products with links to those products. It will be designed as a small web site but scalable as we add more products and services to our repertoire.

Please see the PDF in the uploaded files/media for more information on colors and basic guidelines, but be creative for sure.

Target Market(s)

General

Industry/Entity Type

Technology, Software

Coding

Coded - Design and coding required

Font styles to use
Other font styles liked:
• Goliath, Roboto

Colors
FFC000
F8CF3A
FAE287
FDF2CF
FEFAEE

Requirements
Must have
• Home page template, interior template, News/Press release template
Nice to have
• Searchable
Should not have
• carousels, one-page design

```html
<!DOCTYPE html>
<html lang="en">
<head>
<meta charset="utf-8">
<title>QuartzNook Works, LLC – Home and About Templates</title>
<link href="https://fonts.googleapis.com/css2?family=Montserrat:wght@400;500;600&family=Poppins:wght@500;600;700;800&display=swap" rel="stylesheet">
<style>
:root{
  --board:#7f86c4;
  --purple:#7c82c2;
  --orange:#f7941d;
  --orange-soft:#f8c27e;
  --ink:#111111;
  --grey:#8a8a8a;
  --night:#11121f;
  --white:#ffffff;
  --hero-a:#1e2330;
  --hero-b:#4a4038;
  --about-a:#123048;
  --about-b:#2f6a8c;
}
*{margin:0;padding:0;box-sizing:border-box}
html,body{width:834px;height:1200px;overflow:hidden;background:var(--board)}
body{font-family:"Montserrat",sans-serif;color:var(--ink)}
.board{position:absolute;left:0;top:0;width:1596px;height:2297px;transform:scale(.52256);transform-origin:0 0;background:var(--board)}
.board-label{position:absolute;font-family:"Montserrat",sans-serif;font-weight:500;font-size:40px;color:var(--white);letter-spacing:.5px;transform:translateX(-50%);white-space:nowrap}
.page{position:absolute;width:693px;background:var(--white);overflow:hidden;box-shadow:0 10px 30px rgba(20,20,60,.25)}
.abs{position:absolute}
.hero-art{position:absolute;left:0;top:0}
/* nav */
.nav{position:absolute;left:49px;top:8px;width:590px;height:62px;background:var(--white);border-radius:8px;box-shadow:0 4px 14px rgba(0,0,0,.15)}
.brand{position:absolute;left:22px;top:22px;font-family:"Poppins",sans-serif;font-weight:700;font-size:14px;line-height:18px;color:var(--orange);display:flex;align-items:center;gap:6px;white-space:nowrap}
.brand i{width:9px;height:9px;background:var(--orange);border-radius:50%;display:block}
.menu{position:absolute;left:154px;top:35px;display:flex;font-size:10px;font-weight:500;white-space:nowrap}
.menu span{margin-right:21px}
.menu .on{color:var(--purple)}
.pill{position:absolute;top:-8px;height:24px;font-size:8.5px;font-weight:600;color:var(--white);display:flex;align-items:center;gap:7px;padding-left:14px;white-space:nowrap;overflow:hidden}
.pill.mail{left:354px;width:130px;background:var(--purple);border-radius:6px 0 0 6px}
.pill.call{left:484px;width:110px;background:var(--orange);border-radius:0 6px 6px 0;padding-left:16px}
/* hero text */
.eyebrow{font-family:"Poppins",sans-serif;font-weight:600;font-size:10px;color:var(--white)}
.hero-title{font-family:"Poppins",sans-serif;font-weight:800;color:var(--white);line-height:32px;font-size:33px}
.hero-text{font-size:10.5px;line-height:16px;color:var(--white)}
.btn{position:absolute;height:30px;display:flex;align-items:center;justify-content:center;gap:10px;font-family:"Poppins",sans-serif;font-size:9.5px;font-weight:600;border-radius:2px;transform:skewX(-8deg);white-space:nowrap}
.btn > *{transform:skewX(8deg)}
.btn.solid{background:var(--orange);color:var(--white)}
.btn.line{border:1.5px solid var(--orange);color:var(--orange);background:var(--white)}
/* sections */
.sec-title{font-family:"Poppins",sans-serif;font-weight:700;font-size:21px;text-align:center;transform:translateX(-50%);white-space:nowrap}
.sec-lead{font-size:10.5px;line-height:16px;color:var(--grey);text-align:center;transform:translateX(-50%)}
.num{font-family:"Poppins",sans-serif;font-weight:700;font-size:30px;color:#e4e4e4}
.sliver{position:absolute;width:10px;height:60px;background:var(--orange);transform:skewY(-30deg)}
.photo-round{position:absolute;border-radius:50%;box-shadow:-5px 7px 0 var(--orange-soft),0 16px 30px rgba(0,0,0,.08)}
.half-top{position:absolute;background:var(--purple);border-radius:200px 200px 0 0}
.half-bot{position:absolute;background:var(--orange);border-radius:0 0 200px 200px}
.feat-title{font-family:"Poppins",sans-serif;font-weight:600;font-size:13px;line-height:18px}
.body-grey{font-size:10.5px;line-height:16px;color:var(--grey)}
.tags{position:absolute;display:flex;gap:22px;align-items:center}
.tag{display:flex;align-items:center;gap:12px;font-family:"Poppins",sans-serif;font-size:10px;font-weight:600;white-space:nowrap}
.tag b{width:32px;height:32px;border-radius:5px;display:flex;align-items:center;justify-content:center}
.tag b.o{background:var(--orange)}
.tag b.p{background:var(--purple)}
/* footer */
.footer{position:absolute;left:0;width:693px;height:340px}
.foot-head{position:absolute;font-family:"Poppins",sans-serif;font-weight:700;font-size:11.5px;color:var(--orange)}
.foot-links{position:absolute;font-size:10.5px;line-height:20px;color:var(--white);list-style:none}
.contact{position:absolute;left:212px;display:flex;gap:12px;align-items:flex-start}
.contact .ring{width:30px;height:30px;border:1px solid #3a3b4c;border-radius:50%;display:flex;align-items:center;justify-content:center;margin-top:4px}
.contact small{display:block;font-size:9px;font-weight:600;color:var(--purple)}
.contact span{font-size:10.5px;color:var(--white)}
.foot-text{position:absolute;font-size:10.5px;line-height:16px;color:var(--white)}
.field{position:absolute;left:455px;height:30px;width:155px;background:#222334;font-size:9px;color:#6b6c7c;padding:10px 12px}
.field-go{position:absolute;left:610px;width:33px;height:30px;background:var(--orange);display:flex;align-items:center;justify-content:center}
.socials{position:absolute;left:455px;display:flex;gap:5px}
.socials i{width:30px;height:30px;border-radius:50%;background:var(--purple);display:block;position:relative}
.socials i::after{content:"";position:absolute;left:12px;top:12px;width:6px;height:6px;border-radius:50%;background:var(--white)}
.foot-rule{position:absolute;left:49px;width:595px;height:1px;background:#2a2b3a}
.copy{position:absolute;left:0;width:693px;text-align:center;font-size:9.5px;color:var(--white)}
/* about */
.about-head{font-family:"Poppins",sans-serif;font-weight:700;font-size:20px;line-height:27px}
.value{position:absolute;top:796px;width:186px;height:206px;background:var(--white);box-shadow:0 6px 20px rgba(0,0,0,.07);transform:skewX(-3deg)}
.value-in{transform:skewX(3deg);text-align:center;padding-top:22px}
.value h4{font-family:"Poppins",sans-serif;font-weight:600;font-size:11.5px;margin-top:10px}
.value p{font-size:9.5px;line-height:16px;color:var(--grey);margin:6px 14px 0}
.value .bar{width:74px;height:2px;margin:16px auto 0;background:linear-gradient(90deg,var(--purple) 50%,var(--orange) 50%)}
.ticks{position:absolute;list-style:none;font-size:10.5px;color:var(--grey);line-height:29.5px}
.ticks li{display:flex;align-items:center;gap:6px;white-space:nowrap}
.ticks li::before{content:"";width:9px;height:9px;border-radius:50%;background:var(--orange)}
</style>
</head>
<body>
<div class="board">

  <div class="board-label" style="left:419px;top:112px">Home Page</div>
  <div class="board-label" style="left:1177px;top:258px">About Page</div>

  <!-- HOME TEMPLATE -->
  <section class="page" style="left:73px;top:192px;height:1981px">
    <svg class="hero-art" width="693" height="460" viewBox="0 0 693 460">
      <defs>
        <linearGradient id="heroHome" x1="0" y1="0" x2="1" y2="1">
          <stop offset="0" stop-color="var(--hero-a)"/>
          <stop offset=".6" stop-color="#2a2a30"/>
          <stop offset="1" stop-color="var(--hero-b)"/>
        </linearGradient>
      </defs>
      <polygon points="0,0 693,0 693,383 0,430" fill="url(#heroHome)" role="img" aria-label="Photo of two software developers looking at a monitor in a dark office"/>
      <polygon points="0,430 693,383 693,392 22,450 0,436" fill="var(--purple)"/>
    </svg>

    <nav class="nav">
      <div class="pill mail"><svg width="11" height="8" viewBox="0 0 11 8"><rect x=".5" y=".5" width="10" height="7" fill="none" stroke="#fff"/><path d="M.5 .5 5.5 4.5 10.5 .5" fill="none" stroke="#fff"/></svg>info@qnworks.com</div>
      <div class="pill call"><svg width="10" height="10" viewBox="0 0 10 10"><path d="M2 0.5 4 3 3 4.2C3.8 5.8 4.5 6.5 5.8 7L7 6 9.5 8 8.5 9.5C4 9 1 6 .5 1.5Z" fill="#fff"/></svg>123-456-7890</div>
      <div class="brand"><i></i>QuartzNook</div>
      <div class="menu"><span>Home</span><span>About</span><span>Products</span><span>Projects</span><span>Contributions</span><span>News ▾</span><span>Privacy</span></div>
    </nav>

    <div class="abs eyebrow" style="left:49px;top:125px">Best Organization For</div>
    <h1 class="abs hero-title" style="left:49px;top:142px">software &amp;<br>applications<br>development</h1>
    <p class="abs hero-text" style="left:49px;top:247px;width:300px">QuartzNook Works, LLC is a software and applications development organization that produces client, software as a service (SaaS) products and contributed works for other entities such as site builders and content hubs.</p>
    <div class="btn solid" style="left:50px;top:323px;width:104px"><span>View More</span><svg width="14" height="8" viewBox="0 0 14 8"><path d="M0 4H12M9 1 12 4 9 7" fill="none" stroke="#fff" stroke-width="1.4"/></svg></div>
    <div class="abs" style="left:340px;top:384px;width:13px;height:20px;border-radius:7px;background:var(--white)"></div>

    <h2 class="abs sec-title" style="left:346px;top:490px">The Project Features</h2>
    <p class="abs sec-lead" style="left:346px;top:524px;width:320px">Exercitation ullamco laboris nisi ut aliquip ex ea commodo consequa duis aute irure dolor in reprehenderit in voluptate velit esse cillum dolore eu fugiat nulla pariatur.</p>

    <!-- feature 1 -->
    <div class="abs num" style="left:47px;top:610px">1</div>
    <div class="sliver" style="left:-2px;top:690px"></div>
    <div class="photo-round" role="img" aria-label="Photo of hands holding a smartphone with floating app screens" style="left:66px;top:627px;width:218px;height:218px;background:radial-gradient(circle at 45% 45%,#a87e62,#5e4232)"></div>
    <div class="half-bot" style="left:214px;top:618px;width:28px;height:14px"></div>
    <div class="half-top" style="left:212px;top:632px;width:80px;height:40px"></div>
    <div class="half-bot" style="left:277px;top:677px;width:28px;height:14px"></div>
    <h3 class="abs feat-title" style="left:367px;top:642px">Mobile App<br>Development Practices</h3>
    <p class="abs body-grey" style="left:367px;top:686px;width:262px">Lorem ipsum dolor sit amet, consectetur adipisici elit, sed do eiusmod tempor incididunt ut labores et dolore magna aliqua. Ut enim ad minim venia quis nostrud exercitation ullamco laboris nisi ut aliquip ex ea commodo consequat.</p>
    <div class="tags" style="left:367px;top:782px">
      <div class="tag"><b class="o"><svg width="14" height="16" viewBox="0 0 14 16"><rect x="1" y="1" width="12" height="14" rx="2" fill="none" stroke="#fff" stroke-width="1.6"/></svg></b>Phone Apps</div>
      <div class="tag"><b class="p"><svg width="16" height="14" viewBox="0 0 16 14"><rect x="1" y="1" width="14" height="12" rx="2" fill="none" stroke="#fff" stroke-width="1.6"/></svg></b>Tablet Apps</div>
    </div>

    <!-- feature 2 -->
    <div class="abs num" style="left:625px;top:912px">2</div>
    <div class="sliver" style="left:686px;top:990px"></div>
    <h3 class="abs feat-title" style="left:49px;top:945px">Enterprise<br>Software Development</h3>
    <p class="abs body-grey" style="left:49px;top:988px;width:262px">Lorem ipsum dolor sit amet, consectetur adipisici elit, sed do eiusmod tempor incididunt ut labores et dolore magna aliqua. Ut enim ad minim venia quis nostrud exercitation ullamco laboris nisi ut aliquip ex ea commodo consequat.</p>
    <div class="tags" style="left:49px;top:1085px;gap:38px">
      <div class="tag"><b class="o"><svg width="16" height="10" viewBox="0 0 16 10"><ellipse cx="8" cy="5" rx="7" ry="4" fill="none" stroke="#fff" stroke-width="1.6"/></svg></b>Server Code</div>
      <div class="tag"><b class="p"><svg width="16" height="16" viewBox="0 0 16 16"><circle cx="8" cy="8" r="2" fill="#fff"/><circle cx="8" cy="8" r="6" fill="none" stroke="#fff" stroke-width="1.4"/></svg></b>Web Interfaces</div>
    </div>
    <div class="photo-round" role="img" aria-label="Photo of a developer in front of screens with code" style="left:392px;top:928px;width:220px;height:220px;background:radial-gradient(circle at 55% 40%,#8a8d92,#3a3f46)"></div>
    <div class="half-bot" style="left:436px;top:920px;width:28px;height:14px"></div>
    <div class="half-top" style="left:385px;top:934px;width:82px;height:41px"></div>
    <div class="half-bot" style="left:372px;top:978px;width:28px;height:14px"></div>

    <!-- feature 3 -->
    <div class="abs num" style="left:47px;top:1214px">3</div>
    <div class="sliver" style="left:-2px;top:1290px"></div>
    <div class="photo-round" role="img" aria-label="Photo of hands using a tablet showing a hotel booking screen" style="left:66px;top:1232px;width:218px;height:218px;background:radial-gradient(circle at 40% 40%,#b08868,#5c4434)"></div>
    <div class="half-bot" style="left:214px;top:1222px;width:28px;height:14px"></div>
    <div class="half-top" style="left:212px;top:1236px;width:80px;height:40px"></div>
    <div class="half-bot" style="left:277px;top:1281px;width:28px;height:14px"></div>
    <h3 class="abs feat-title" style="left:367px;top:1246px">Hotel Reservation,<br>Packages &amp; Services Portal</h3>
    <p class="abs body-grey" style="left:367px;top:1290px;width:262px">Lorem ipsum dolor sit amet, consectetur adipisici elit, sed do eiusmod tempor incididunt ut labores et dolore magna aliqua. Ut enim ad minim venia quis nostrud exercitation ullamco laboris nisi ut aliquip ex ea commodo consequat.</p>
    <div class="tags" style="left:367px;top:1387px">
      <div class="tag"><b class="o"><svg width="16" height="16" viewBox="0 0 16 16"><circle cx="8" cy="8" r="6" fill="none" stroke="#fff" stroke-width="1.6"/></svg></b>Site Builder</div>
      <div class="tag"><b class="p"><svg width="14" height="16" viewBox="0 0 14 16"><path d="M7 1C9 5 12 7 12 10A5 5 0 0 1 2 10C2 7 5 5 7 1Z" fill="none" stroke="#fff" stroke-width="1.5"/></svg></b>Content Hub</div>
    </div>

    <div class="btn line" style="left:296px;top:1508px;width:102px"><span>View More</span><svg width="14" height="8" viewBox="0 0 14 8"><path d="M0 4H12M9 1 12 4 9 7" fill="none" stroke="#f7941d" stroke-width="1.4"/></svg></div>
    <p class="abs sec-lead" style="left:346px;top:1557px;width:320px">Exercitation ullamco laboris nisi ut aliquip ex ea commodo consequa duis aute irure dolor in reprehenderit in voluptate velit esse cillum dolore eu fugiat nulla pariatur.</p>

    <footer class="footer" style="top:1641px">
      <svg class="abs" style="left:0;top:0" width="693" height="340" viewBox="0 0 693 340">
        <polygon points="0,28 28,5 693,47 693,52 0,28" fill="var(--purple)"/>
        <polygon points="0,28 693,52 693,340 0,340" fill="var(--night)"/>
      </svg>
      <div class="foot-head" style="left:49px;top:80px">Quick Links</div>
      <ul class="foot-links" style="left:49px;top:100px"><li>Home</li><li>About</li><li>Products</li><li>Projects</li><li>Contributions</li><li>News</li><li>Privacy</li></ul>
      <div class="foot-head" style="left:212px;top:80px">Contact Details</div>
      <div class="contact" style="top:102px"><div class="ring"><svg width="11" height="8" viewBox="0 0 11 8"><rect x=".5" y=".5" width="10" height="7" fill="none" stroke="#aaa"/><path d="M.5 .5 5.5 4.5 10.5 .5" fill="none" stroke="#aaa"/></svg></div><div><small>Email:</small><span>info@qnworks.com</span></div></div>
      <div class="contact" style="top:151px"><div class="ring"><svg width="10" height="10" viewBox="0 0 10 10"><path d="M2 .5 4 3 3 4.2C3.8 5.8 4.5 6.5 5.8 7L7 6 9.5 8 8.5 9.5C4 9 1 6 .5 1.5Z" fill="#aaa"/></svg></div><div><small>Phone:</small><span>123-456-7890</span></div></div>
      <div class="contact" style="top:200px"><div class="ring"><svg width="10" height="10" viewBox="0 0 10 10"><path d="M2 .5 4 3 3 4.2C3.8 5.8 4.5 6.5 5.8 7L7 6 9.5 8 8.5 9.5C4 9 1 6 .5 1.5Z" fill="#aaa"/></svg></div><div><small>Phone:</small><span>123-456-7890</span></div></div>
      <div class="foot-head" style="left:455px;top:80px">Subscribe Newsletter</div>
      <p class="foot-text" style="left:455px;top:101px;width:190px">Exercitation ullamco laboris nisi ut aliquip xercitation ullamco</p>
      <div class="field" style="top:151px">Email address</div>
      <div class="field-go" style="top:151px"><svg width="14" height="8" viewBox="0 0 14 8"><path d="M0 4H12M9 1 12 4 9 7" fill="none" stroke="#fff" stroke-width="1.4"/></svg></div>
      <div class="socials" style="top:205px"><i></i><i></i><i></i><i></i></div>
      <div class="foot-rule" style="top:292px"></div>
      <div class="copy" style="top:310px">Copyright © 2023 QuartzNook Works, LLC</div>
    </footer>
  </section>

  <!-- ABOUT TEMPLATE -->
  <section class="page" style="left:830px;top:340px;height:1833px">
    <svg class="hero-art" width="693" height="310" viewBox="0 0 693 310">
      <defs>
        <linearGradient id="heroAbout" x1="0" y1="0" x2="1" y2="1">
          <stop offset="0" stop-color="var(--about-a)"/>
          <stop offset=".55" stop-color="#1d4a68"/>
          <stop offset="1" stop-color="var(--about-b)"/>
        </linearGradient>
      </defs>
      <polygon points="0,0 693,0 693,233 0,285" fill="url(#heroAbout)" role="img" aria-label="Photo of a developer working at night with code lines overlaid"/>
      <polygon points="0,285 693,233 693,240 22,302 0,290" fill="var(--purple)"/>
    </svg>

    <nav class="nav">
      <div class="pill mail"><svg width="11" height="8" viewBox="0 0 11 8"><rect x=".5" y=".5" width="10" height="7" fill="none" stroke="#fff"/><path d="M.5 .5 5.5 4.5 10.5 .5" fill="none" stroke="#fff"/></svg>info@qnworks.com</div>
      <div class="pill call"><svg width="10" height="10" viewBox="0 0 10 10"><path d="M2 0.5 4 3 3 4.2C3.8 5.8 4.5 6.5 5.8 7L7 6 9.5 8 8.5 9.5C4 9 1 6 .5 1.5Z" fill="#fff"/></svg>123-456-7890</div>
      <div class="brand"><i></i>QuartzNook</div>
      <div class="menu"><span>Home</span><span class="on">About</span><span>Products</span><span>Projects</span><span>Contributions</span><span>News ▾</span><span>Privacy</span></div>
    </nav>

    <h1 class="abs hero-title" style="left:49px;top:112px">About us</h1>
    <p class="abs hero-text" style="left:49px;top:160px;width:240px">Lorem ipsum dolor sit amet consectetur adis pisicing elit, sed do eiusmod tempor incidi it dunt ut labore et dolore magna aliqua utter enim ad minim veniam sed.</p>

    <svg class="abs" style="left:40px;top:340px" width="290" height="320" viewBox="0 0 290 320">
      <defs>
        <linearGradient id="teamA" x1="0" y1="0" x2="1" y2="1"><stop offset="0" stop-color="#3d5a72"/><stop offset="1" stop-color="#1e2e3c"/></linearGradient>
        <linearGradient id="teamB" x1="0" y1="0" x2="1" y2="1"><stop offset="0" stop-color="#c9c6c2"/><stop offset="1" stop-color="#6f7a84"/></linearGradient>
      </defs>
      <polygon points="37,8 254,8 238,288 9,288" fill="url(#teamA)" role="img" aria-label="Photo of a smiling developer at a laptop"/>
      <polygon points="170,186 281,186 269,312 156,312" fill="#fff"/>
      <polygon points="173,188 278,188 266,310 159,310" fill="url(#teamB)" role="img" aria-label="Photo of a smiling colleague wearing glasses"/>
    </svg>

    <h2 class="abs about-head" style="left:358px;top:342px">We are best in<br>software &amp; applications<br>development</h2>
    <p class="abs body-grey" style="left:358px;top:429px;width:290px">Exercitation ullamco laboris nisi ut aliquip ex ea comod o consequa duis aute irure dolor in reprehenderit in vol ptate velit esse cillum dolore eu fugiat nulla pariatur.</p>
    <p class="abs body-grey" style="left:358px;top:492px;width:290px">Duis aute irure dolor in reprehenderit in voluptate velit esse cillum dolore eu fugiat nulla pariatur. Excepteur sint occa ecat cupidatat non proident, sunt.</p>
    <p class="abs body-grey" style="left:358px;top:555px;width:290px">Excepteur sint occaecat cupidatat non proident, sunte in culpa qui officia deserunt mollit anim id est laborius um ed ut perspiciatis unde omnis iste natus.</p>

    <h2 class="abs sec-title" style="left:347px;top:702px">Core Values</h2>
    <p class="abs sec-lead" style="left:347px;top:732px;width:320px">Exercitation ullamco laboris nisi ut aliquip ex ea comodo consequa duis aute irure dolor in reprehenderit</p>

    <div class="value" style="left:58px"><div class="value-in">
      <svg width="50" height="36" viewBox="0 0 50 36" fill="none" stroke="var(--purple)" stroke-width="1.6"><circle cx="13" cy="8" r="5"/><circle cx="25" cy="8" r="5"/><circle cx="37" cy="8" r="5"/><path d="M4 24C4 18 22 18 22 24M28 24C28 18 46 18 46 24"/><path d="M19 24 25 20 31 24 25 34Z" stroke="var(--orange)"/></svg>
      <h4>Integrity</h4>
      <p>Exercitation ullamco laboris ut nisi ut aliquip ex ea comodop consequa duis aute irure sedi ut dolor in reprehenderit.</p>
      <div class="bar"></div></div></div>
    <div class="value" style="left:252px"><div class="value-in">
      <svg width="50" height="44" viewBox="0 0 50 44" fill="none" stroke="var(--purple)" stroke-width="1.6"><circle cx="17" cy="12" r="4"/><circle cx="33" cy="12" r="4"/><path d="M6 40V24L17 20 25 28 33 20 44 24V40"/><path d="M25 2V6M19 4 21 7M31 4 29 7" stroke="var(--orange)"/></svg>
      <h4>Build Relationships</h4>
      <p>Exercitation ullamco laboris ut nisi ut aliquip ex ea comodop consequa duis aute irure sedi ut dolor in reprehenderit.</p>
      <div class="bar"></div></div></div>
    <div class="value" style="left:446px"><div class="value-in">
      <svg width="50" height="44" viewBox="0 0 50 44" fill="none" stroke="var(--purple)" stroke-width="1.6"><rect x="6" y="28" width="6" height="14"/><rect x="16" y="22" width="6" height="20"/><rect x="26" y="18" width="6" height="24"/><rect x="36" y="14" width="6" height="28"/><circle cx="38" cy="6" r="4" stroke="var(--orange)"/><circle cx="12" cy="8" r="3"/></svg>
      <h4>Working Hard</h4>
      <p>Exercitation ullamco laboris ut nisi ut aliquip ex ea comodop consequa duis aute irure sedi ut dolor in reprehenderit.</p>
      <div class="bar"></div></div></div>

    <h2 class="abs" style="left:49px;top:1132px;font-family:'Poppins',sans-serif;font-weight:700;font-size:21px">Our Mission</h2>
    <p class="abs body-grey" style="left:49px;top:1164px;width:280px">Exercitation ullamco laboris nisi ut aliquip ex eacom odo consequa duis aute irure dolor in reprehen derit in vol ptate velit esse cillum dolore eu fugiat nulla se Duis aute irure dolor in reprehe nderit in voluptate velit esse cillum dolore eu fugiat nulla.</p>
    <ul class="ticks" style="left:49px;top:1253px"><li>cillum dolore eu fug</li><li>cillum dolore eu fug</li><li>cillum dolore eu fug</li></ul>
    <ul class="ticks" style="left:193px;top:1253px"><li>Rure dolor in reprehe</li><li>Rure dolor in reprehe</li><li>Rure dolor in reprehe</li></ul>
    <div class="btn solid" style="left:53px;top:1360px;width:120px"><span>View Products</span><svg width="14" height="8" viewBox="0 0 14 8"><path d="M0 4H12M9 1 12 4 9 7" fill="none" stroke="#fff" stroke-width="1.4"/></svg></div>

    <div class="photo-round" role="img" aria-label="Photo of a smiling developer with headphones behind floating code" style="left:390px;top:1104px;width:254px;height:254px;background:radial-gradient(circle at 60% 40%,#3f8aa8,#163a52)"></div>
    <div class="half-top" style="left:346px;top:1120px;width:92px;height:46px"></div>
    <div class="half-bot" style="left:352px;top:1172px;width:32px;height:16px"></div>
    <div class="half-bot" style="left:610px;top:1325px;width:32px;height:9px;background:var(--purple)"></div>
    <div class="half-bot" style="left:610px;top:1337px;width:32px;height:16px"></div>

    <footer class="footer" style="top:1493px">
      <svg class="abs" style="left:0;top:0" width="693" height="340" viewBox="0 0 693 340">
        <polygon points="0,28 28,5 693,47 693,52 0,28" fill="var(--purple)"/>
        <polygon points="0,28 693,52 693,340 0,340" fill="var(--night)"/>
      </svg>
      <div class="foot-head" style="left:49px;top:80px">Quick Links</div>
      <ul class="foot-links" style="left:49px;top:100px"><li>Home</li><li>About</li><li>Products</li><li>Projects</li><li>Contributions</li><li>News</li><li>Privacy</li></ul>
      <div class="foot-head" style="left:212px;top:80px">Contact Details</div>
      <div class="contact" style="top:102px"><div class="ring"><svg width="11" height="8" viewBox="0 0 11 8"><rect x=".5" y=".5" width="10" height="7" fill="none" stroke="#aaa"/><path d="M.5 .5 5.5 4.5 10.5 .5" fill="none" stroke="#aaa"/></svg></div><div><small>Email:</small><span>info@qnworks.com</span></div></div>
      <div class="contact" style="top:151px"><div class="ring"><svg width="10" height="10" viewBox="0 0 10 10"><path d="M2 .5 4 3 3 4.2C3.8 5.8 4.5 6.5 5.8 7L7 6 9.5 8 8.5 9.5C4 9 1 6 .5 1.5Z" fill="#aaa"/></svg></div><div><small>Phone:</small><span>123-456-7890</span></div></div>
      <div class="contact" style="top:200px"><div class="ring"><svg width="10" height="10" viewBox="0 0 10 10"><path d="M2 .5 4 3 3 4.2C3.8 5.8 4.5 6.5 5.8 7L7 6 9.5 8 8.5 9.5C4 9 1 6 .5 1.5Z" fill="#aaa"/></svg></div><div><small>Phone:</small><span>123-456-7890</span></div></div>
      <div class="foot-head" style="left:455px;top:80px">Subscribe Newsletter</div>
      <p class="foot-text" style="left:455px;top:101px;width:190px">Exercitation ullamco laboris nisi ut aliquip xercitation ullamco</p>
      <div class="field" style="top:151px">Email address</div>
      <div class="field-go" style="top:151px"><svg width="14" height="8" viewBox="0 0 14 8"><path d="M0 4H12M9 1 12 4 9 7" fill="none" stroke="#fff" stroke-width="1.4"/></svg></div>
      <div class="socials" style="top:205px"><i></i><i></i><i></i><i></i></div>
      <div class="foot-rule" style="top:292px"></div>
      <div class="copy" style="top:310px">Copyright © 2023 QuartzNook Works, LLC</div>
    </footer>
  </section>

</div>
</body>
</html>
```